Company Web Design Project

Velmora links works in the market of renewable energy with energy monitoring systems.

Velmora-link wants a light and easy company website that informs about our core business and our products as well as the company. The sites should work on multiple platforms. It should include pictures and possibilities for news.
You find elements and company information on the following links:

http://velmora-link.example/english-version/index.htm
some productinformation you find on this site:
http://quorvane.example/

Velmora-link AG is also interested in a Powerpoint template that matches the new website design as well as businesscards and a letter template.

Some more information about the company.

Headquartered in Karlsruhe, Germany, Velmora-Link AG manufactures hardware & software solutions for remote monitoring, analysis, and control of electrical installations, alarm systems, and other critical networks.

In addition, our company provides test, measurement, and control equipment for use in a wide range of industrial and biological processes.

Founded in the year 2000, Velmora-Link AG has established a comprehensive service network. Our solutions and systems are in operation e.g. in Europe, USA, Brazil, and Asia.

Velmora-Link's team of experienced engineers, physicists, and network specialists continuously develop innovative solutions for many key industries - particularly in the renewable energies field.

To ensure the operational safety of their plants by means of optimized real time fault analysis routines

for process optimization

for a measurable increase in yield from production and trade.

Our products are distributed globally via an international dealer network.

In the interest of our customers and their needs, our aim is to expand this dealer network even more.

Target Market(s)

large solar project companies like, large renewable energy investors, large wholesellers for renewable energy, producer of solar panels.

Industry/Entity Type

Electrical

Requirements
Must have
• responsive design for multiple platforms

```html
<!DOCTYPE html>
<html lang="en">
<head>
<meta charset="utf-8">
<title>Velmora-link – Interactive Technology</title>
<link rel="stylesheet" href="https://fonts.googleapis.com/css2?family=PT+Sans+Narrow:wght@400;700&family=Source+Sans+3:wght@400;600&display=swap">
<style>
  :root{
    --green:#0b6b57;
    --green-dark:#064a3c;
    --green-light:#13917a;
    --heading:#0d5f4d;
    --text:#3a3a3a;
    --page:#f2f2f2;
    --white:#ffffff;
    --border:#dcdcdc;
    --footer-top:#5a5a5a;
    --footer-bottom:#2e2e2e;
    --social-1:#3b5a9a;
    --social-2:#3aa9e0;
    --social-3:#1f77b4;
    --social-4:#f08a24;
  }
  *{box-sizing:border-box;margin:0;padding:0}
  html,body{width:1200px;height:1159px;overflow:hidden}
  body{background:var(--page);font-family:"Source Sans 3",sans-serif;color:var(--text);position:relative;border-top:3px solid #333}
  .page{position:relative;width:1200px;height:1156px}
  a{color:inherit;text-decoration:none}

  .brand{position:absolute;left:155px;top:22px;display:flex;align-items:center;gap:10px}
  .brand-square{width:38px;height:38px;background:var(--green)}
  .brand-name{font-weight:600;font-size:30px;color:#222;letter-spacing:-.5px}

  .util-nav{position:absolute;right:152px;top:14px;display:flex;font-size:12px;color:#333}
  .util-nav a{padding:0 6px;border-left:1px solid #999;line-height:16px}
  .util-nav a:first-child{border-left:none}
  .util-nav a:last-child{padding-right:0}

  .search{position:absolute;left:910px;top:50px;width:136px;height:28px;background:var(--white);border:1px solid #cfcfcf;display:flex;align-items:center;padding-left:9px;gap:6px;font-size:11.5px;color:#444}

  .main-nav{position:absolute;left:153px;top:100px;width:893px;height:29px;display:flex;background:linear-gradient(#13917a,#0b6b57 55%,#064a3c)}
  .main-nav a{font-family:"PT Sans Narrow",sans-serif;font-size:16px;color:var(--white);text-transform:uppercase;display:flex;align-items:center;justify-content:center;border-left:1px solid #b9d9d0}
  .main-nav a:first-child{border-left:none}

  .slider{position:absolute;left:152px;top:137px;width:895px;height:341px;background:var(--white);border:1px solid #ddd}
  .slider-shadow{position:absolute;left:210px;top:478px;width:780px;height:30px;background:radial-gradient(ellipse at top,rgba(0,0,0,.28),rgba(0,0,0,0) 70%)}
  .slide-photo{position:absolute;left:5px;top:4px;width:883px;height:333px;
    background:
      radial-gradient(ellipse 260px 120px at 640px 80px,rgba(140,190,70,.45),rgba(140,190,70,0) 70%),
      radial-gradient(ellipse 380px 260px at 650px 190px,#f4f5f6,rgba(244,245,246,0) 75%),
      radial-gradient(ellipse 160px 90px at 460px 300px,rgba(225,170,140,.7),rgba(225,170,140,0) 70%),
      linear-gradient(100deg,#c9c9c6 0%,#d6d6d3 35%,#e4e5e5 55%,#eeefef 80%,#e3e4e4 100%)}
  .slide-caption{position:absolute;left:19px;top:262px;width:202px;height:52px;background:rgba(110,110,110,.75);color:var(--white);font-family:"PT Sans Narrow",sans-serif;font-size:30px;display:flex;align-items:center;padding-left:16px}
  .slide-dots{position:absolute;left:415px;top:310px;width:67px;height:27px;background:var(--white);display:flex;align-items:center;justify-content:center;gap:6px}
  .slide-dots span{width:7px;height:7px;border-radius:50%;background:#c8c8c8}
  .slide-dots span.active{background:var(--green-dark)}

  .feature{position:absolute;top:512px;width:215px}
  .feature h2{font-family:"PT Sans Narrow",sans-serif;font-weight:400;font-size:22px;color:var(--heading);height:33px}
  .feature-frame{width:215px;height:168px;background:var(--white);border:1px solid var(--border);padding:4px}
  .feature-photo{width:100%;height:100%}
  .feature p{margin-top:10px;font-size:13px;line-height:18.5px;text-align:justify}
  .btn-more{display:inline-flex;align-items:center;justify-content:center;margin:7px 0 0 3px;width:52px;height:27px;background:linear-gradient(#13917a,#064a3c);color:var(--white);font-family:"PT Sans Narrow",sans-serif;font-size:15px;text-transform:uppercase}

  .welcome{position:absolute;left:157px;top:848px;width:891px;height:221px;background:var(--white);border:1px solid var(--border)}
  .welcome h1{position:absolute;left:14px;top:13px;font-family:"PT Sans Narrow",sans-serif;font-weight:400;font-size:21px;color:var(--heading)}
  .welcome-text{position:absolute;left:14px;top:46px;width:632px;font-size:13px;line-height:18.5px;text-align:justify}
  .welcome-text p{margin-bottom:8px}
  .welcome-photo{position:absolute;left:663px;top:48px;width:206px;height:145px;
    background:
      radial-gradient(ellipse 60px 80px at 35px 80px,rgba(40,40,50,.75),rgba(40,40,50,0) 80%),
      radial-gradient(ellipse 70px 80px at 170px 95px,rgba(120,160,200,.75),rgba(120,160,200,0) 80%),
      linear-gradient(135deg,#efece7,#d9d2c7 50%,#c4ccd4)}

  .footer{position:absolute;left:0;top:1077px;width:1200px;height:82px;background:linear-gradient(var(--footer-top),var(--footer-bottom));color:#eee;font-size:12.5px}
  .follow{position:absolute;left:157px;top:24px}
  .social{position:absolute;left:157px;top:47px;display:flex;gap:7px}
  .social span{width:16px;height:16px;border-radius:2px}
  .footer-nav{position:absolute;right:152px;top:24px;display:flex}
  .footer-nav a{padding:0 8px;border-left:1px solid #bbb;line-height:13px}
  .footer-nav a:first-child{border-left:none}
  .footer-nav a:last-child{padding-right:0}
  .copyright{position:absolute;right:152px;top:45px}
</style>
</head>
<body>
<div class="page">
  <a class="brand" href="#"><span class="brand-square"></span><span class="brand-name">Velmora-link</span></a>

  <nav class="util-nav">
    <a href="#">Your Nearest Dealer</a><a href="#">Registering</a><a href="#">Downloads</a><a href="#">Dates</a><a href="#">Press Releases</a><a href="#">FAQ</a><a href="#">Partners</a><a href="#">Links</a>
  </nav>

  <div class="search">
    <svg width="12" height="12" viewBox="0 0 12 12"><circle cx="4.5" cy="4.5" r="3.3" fill="none" stroke="#666" stroke-width="1.4"/><line x1="7" y1="7" x2="11" y2="11" stroke="#666" stroke-width="1.6"/></svg>
    Search
  </div>

  <nav class="main-nav">
    <a href="#" style="width:124px">Home</a>
    <a href="#" style="width:120px">Company</a>
    <a href="#" style="width:124px">Business Areas</a>
    <a href="#" style="width:131px">Products</a>
    <a href="#" style="width:134px">Topical</a>
    <a href="#" style="width:127px">Service</a>
    <a href="#" style="width:133px">Contact</a>
  </nav>

  <div class="slider-shadow"></div>
  <section class="slider">
    <div class="slide-photo" role="img" aria-label="Photo of a hand pressing keys on a wall-mounted alarm system keypad with a green display"></div>
    <div class="slide-caption">ALARM SYSTEMS</div>
    <div class="slide-dots"><span></span><span class="active"></span><span></span><span></span></div>
  </section>

  <article class="feature" style="left:152px">
    <h2>Remote Monitoring</h2>
    <div class="feature-frame"><div class="feature-photo" role="img" aria-label="Photo of a hand holding a remote control before blurred screens" style="background:radial-gradient(circle at 45% 45%,#e8d6b0,#8a6a45 30%,#2f4650 60%,#121418 95%)"></div></div>
    <p>"The end-use efficiency is the cheapest and most appropriate bridge technol&shy;ogy in a regenerative current era repre&shy;sents," this is one...</p>
    <a class="btn-more" href="#">More</a>
  </article>

  <article class="feature" style="left:379px">
    <h2>Analysis</h2>
    <div class="feature-frame"><div class="feature-photo" role="img" aria-label="Photo of hands reviewing bar charts on a tablet over papers" style="background:radial-gradient(ellipse at 55% 55%,#a9c8e6,rgba(169,200,230,0) 45%),linear-gradient(135deg,#d9c3a0,#f1f1ef 45%,#b4c4d6)"></div></div>
    <p>"The end-use efficiency is the cheapest and most appropriate bridge technol&shy;ogy in a regenerative current era repre&shy;sents," this is one...</p>
    <a class="btn-more" href="#">More</a>
  </article>

  <article class="feature" style="left:606px">
    <h2>Electrical Installations</h2>
    <div class="feature-frame"><div class="feature-photo" role="img" aria-label="Photo of an electrician in a yellow hard hat working at a switch cabinet" style="background:radial-gradient(ellipse at 20% 15%,#f0c020,rgba(240,192,32,0) 30%),radial-gradient(ellipse at 20% 75%,#b8d040,rgba(184,208,64,0) 35%),linear-gradient(110deg,#8fa8c4,#b8a890 40%,#4a4438 70%,#2a2826)"></div></div>
    <p>"The end-use efficiency is the cheapest and most appropriate bridge technol&shy;ogy in a regenerative current era repre&shy;sents," this is one...</p>
    <a class="btn-more" href="#">More</a>
  </article>

  <article class="feature" style="left:833px">
    <h2>Alarm Systems</h2>
    <div class="feature-frame"><div class="feature-photo" role="img" aria-label="Photo of a finger pressing a white alarm keypad" style="background:radial-gradient(ellipse at 80% 75%,#e6b8a0,rgba(230,184,160,0) 40%),radial-gradient(ellipse at 45% 50%,#d8dadc,rgba(216,218,220,0) 45%),linear-gradient(135deg,#fafafa,#eeeeee)"></div></div>
    <p>"The end-use efficiency is the cheapest and most appropriate bridge technol&shy;ogy in a regenerative current era repre&shy;sents," this is one...</p>
    <a class="btn-more" href="#">More</a>
  </article>

  <section class="welcome">
    <h1>Welcome to our site</h1>
    <div class="welcome-text">
      <p>Founded in the year 2000, Velmora-Link AG has established a comprehensive service network. Our solutions and systems are in operation e.g. in Europe, USA, Brazil, and Asia.</p>
      <p>Velmora-Link's team of experienced engineers, physicists, and network specialists continuously develop innovative solutions for many key industries - particularly in the renewable energies field.</p>
      <p>To ensure the operational safety of their plants by means of optimized real time fault analysis routines for process opti&shy;mization for a measurable increase in yield from production and trade. Our products are distributed globally via an international dealer network. In the interest of our customers and their needs, our aim is to expand this dealer network even more.</p>
    </div>
    <div class="welcome-photo" role="img" aria-label="Photo of a business meeting with three people at a table"></div>
  </section>

  <footer class="footer">
    <div class="follow">Follow Us On</div>
    <div class="social" aria-label="Social links">
      <span style="background:var(--social-1)"></span><span style="background:var(--social-2)"></span><span style="background:var(--social-3)"></span><span style="background:var(--social-4)"></span>
    </div>
    <nav class="footer-nav">
      <a href="#">Home</a><a href="#">Company</a><a href="#">Business Areas</a><a href="#">Products</a><a href="#">Topical</a><a href="#">Service</a><a href="#">Contact</a>
    </nav>
    <div class="copyright">Copyrights @2013 All Rights Reserved</div>
  </footer>
</div>
</body>
</html>
```